Mission statement design for a secondary school

We have the content of our mission statement and need an appealing layout. The design should fit on a poster or A4 page. The content grouping in the document should also be graphically recognizable. Our target group are young people and their parents as well as the school staff, which is why we need a modern design that is not out after 2 years. It must be easy to grasp visually and graphically simple.

Target Market(s)

Actors of the school

Requirements
Must have
• cantonal logo including school name see document can be integrated as a header
Should not have
• References to trademarks or third parties

```html
<!DOCTYPE html>
<html lang="de">
<head>
<meta charset="utf-8">
<title>Leitbild – Haltung an unserer Schule</title>
<link href="https://fonts.googleapis.com/css2?family=Poppins:wght@800&family=Roboto:wght@400&display=swap" rel="stylesheet">
<style>
  :root {
    --bg: #dcdcdc;
    --paper: #f1f1f2;
    --ink: #444446;
    --heading: #3d3d3f;
    --band: #414143;
    --accent: #ee2e36;
    --white: #ffffff;
  }
  * { box-sizing: border-box; margin: 0; padding: 0; }
  html, body {
    width: 1180px; height: 1200px; overflow: hidden;
    background: var(--bg);
  }
  .poster {
    position: absolute; left: 186px; top: 21px;
    width: 796px; height: 1141px;
    background: var(--paper);
    transform: scale(1.015); transform-origin: top left;
    box-shadow: 0 10px 30px rgba(0,0,0,.12);
    overflow: hidden;
  }
  .corner-mark {
    position: absolute; left: 48px; top: 0;
    width: 90px; height: 66px; background: var(--accent);
  }
  .section-title {
    position: absolute; left: 49px;
    font-family: "Poppins", sans-serif; font-weight: 800;
    font-size: 54px; line-height: 62px; letter-spacing: -0.5px;
    color: var(--heading);
  }
  .band {
    position: absolute; right: 0; width: 180px; height: 90px;
    background: var(--band); border-radius: 45px 0 0 45px;
  }
  .band .badge {
    position: absolute; left: 5px; top: 5px;
    width: 80px; height: 80px; border-radius: 50%;
    background: var(--accent); border: 3px solid var(--white);
    display: flex; align-items: center; justify-content: center;
  }
  .band .badge svg { width: 42px; height: 42px; }
  .checklist {
    position: absolute; list-style: none;
    font-family: "Roboto", sans-serif; font-size: 13.5px;
    line-height: 16px; color: var(--ink);
  }
  .checklist li {
    position: relative; padding-left: 22px; margin-bottom: 14px;
  }
  .checklist.compact { font-size: 12px; }
  .checklist li svg {
    position: absolute; left: 0; top: 2px; width: 13px; height: 13px;
  }
  .col-left { left: 48px; width: 340px; }
  .col-right { left: 414px; width: 340px; }
</style>
</head>
<body>
<svg width="0" height="0" style="position:absolute">
  <defs>
    <symbol id="tick" viewBox="0 0 14 14">
      <rect x="1" y="1" width="12" height="12" rx="3" fill="none" stroke="#ee2e36" stroke-width="1.5"/>
      <path d="M4 7.2l2.2 2.2L10.2 5" fill="none" stroke="#ee2e36" stroke-width="1.6" stroke-linecap="round" stroke-linejoin="round"/>
    </symbol>
  </defs>
</svg>

<main class="poster">
  <div class="corner-mark"></div>

  <!-- Haltung -->
  <h1 class="section-title" style="top:104px;">Haltung An<br>unserer Schule…</h1>
  <div class="band" style="top:112px;">
    <div class="badge">
      <svg viewBox="0 0 40 40" fill="none" stroke="#fff" stroke-width="2" stroke-linejoin="round">
        <path d="M5 18L20 5l15 13"/><path d="M8 16v18h24V16"/>
        <rect x="11" y="20" width="8" height="7"/><path d="M23 34V22h6v12"/>
      </svg>
    </div>
  </div>
  <ul class="checklist col-left" style="top:256px;">
    <li><svg><use href="#tick"/></svg>… stehen die Lernenden im Mittelpunkt.</li>
    <li><svg><use href="#tick"/></svg>… ist Integration selbstverständlich.</li>
  </ul>
  <ul class="checklist compact col-right" style="top:257px;">
    <li style="margin-bottom:11px;"><svg><use href="#tick"/></svg>… begegnen wir uns respektvoll und wertschätzend.</li>
    <li><svg><use href="#tick"/></svg>… setzen wir uns für lebenslanges Lernen ein.</li>
  </ul>

  <!-- Lernen -->
  <h2 class="section-title" style="top:360px;">Lernen</h2>
  <div class="band" style="top:350px;">
    <div class="badge">
      <svg viewBox="0 0 40 40" fill="none" stroke="#fff" stroke-width="2" stroke-linejoin="round">
        <path d="M4 10v20c6-1 11 0 16 3 5-3 10-4 16-3V10c-6-1-11 0-16 3-5-3-10-4-16-3z"/>
        <path d="M20 13v20"/><path d="M2 14v18h36V14"/>
      </svg>
    </div>
  </div>
  <ul class="checklist col-left" style="top:451px;">
    <li><svg><use href="#tick"/></svg>Wir begleiten unsere Lernenden hin<br>zur Selbständigkeit.</li>
    <li><svg><use href="#tick"/></svg>Wir unterstützen unsere Lernenden in ihrem<br>individuellen Kompetenzerwerb.</li>
    <li><svg><use href="#tick"/></svg>Wir ermöglichen allen Lernenden Erfolge.</li>
    <li><svg><use href="#tick"/></svg>Die Unterrichtsinhalte orientieren sich<br>an aktuellen Themen.</li>
  </ul>
  <ul class="checklist col-right" style="top:450px;">
    <li><svg><use href="#tick"/></svg>Wir beurteilen transparent.</li>
    <li><svg><use href="#tick"/></svg>Wir begegnen Heterogenität mit<br>multiprofessionellen Teams.</li>
    <li><svg><use href="#tick"/></svg>Wir schaffen eine wertschätzende und<br>förderliche Atmosphäre.</li>
    <li><svg><use href="#tick"/></svg>Unsere Schule bietet eine<br>zeitgemässe Infrastruktur.</li>
  </ul>

  <!-- Entwicklung -->
  <h2 class="section-title" style="top:650px;">Entwicklung</h2>
  <div class="band" style="top:629px;">
    <div class="badge">
      <svg viewBox="0 0 40 40" fill="none" stroke="#fff" stroke-width="2" stroke-linejoin="round">
        <rect x="7" y="7" width="26" height="29" rx="1"/>
        <path d="M11 4v6M15 4v6M19 4v6M23 4v6M27 4v6M7 12h26"/>
        <path d="M11 18h3M17 18h12M11 23h3M17 23h12M11 28h3M17 28h12"/>
      </svg>
    </div>
  </div>
  <ul class="checklist col-left" style="top:746px;">
    <li><svg><use href="#tick"/></svg>Wir entwickeln unsere Schule gemeinsam.</li>
    <li><svg><use href="#tick"/></svg>Wir setzen unsere Fähigkeiten und Kräfte gezielt ein.</li>
    <li><svg><use href="#tick"/></svg>Alle tragen Verantwortung.</li>
    <li><svg><use href="#tick"/></svg>Wir lernen alle voneinander.</li>
  </ul>
  <ul class="checklist col-right" style="top:746px;">
    <li><svg><use href="#tick"/></svg>Wir bilden uns kontinuierlich weiter.</li>
    <li><svg><use href="#tick"/></svg>Wir reflektieren unser Handeln.</li>
    <li><svg><use href="#tick"/></svg>Wir sind innovativ und gehen mutig<br>unseren Weg.</li>
  </ul>

  <!-- Gemeinschaft -->
  <h2 class="section-title" style="top:890px;">Gemeinschaft</h2>
  <div class="band" style="top:874px;">
    <div class="badge">
      <svg viewBox="0 0 40 40" fill="none" stroke="#fff" stroke-width="2" stroke-linejoin="round">
        <circle cx="20" cy="11" r="7"/>
        <path d="M5 36c0-9 7-15 15-15s15 6 15 15z"/>
        <path d="M13 23l7 7 7-7"/>
      </svg>
    </div>
  </div>
  <ul class="checklist col-left" style="top:986px;">
    <li><svg><use href="#tick"/></svg>Unsere Schule achtet die Gesundheit aller.</li>
    <li><svg><use href="#tick"/></svg>Wir legen Wert auf eine offene Kommunikation.</li>
    <li><svg><use href="#tick"/></svg>Unsere pädagogische Zusammenarbeit basiert<br>auf einer professionellen Haltung.</li>
  </ul>
  <ul class="checklist col-right" style="top:986px; left:416px;">
    <li><svg><use href="#tick"/></svg>Die Eltern sind ein Teil unserer<br>Schulgemeinschaft und tragen Verantwortung.</li>
    <li><svg><use href="#tick"/></svg>Wir haben an unserer Schule Freiräume<br>innerhalb klarer Rahmenbedingungen.</li>
  </ul>
</main>
</body>
</html>
```